Nine Moons Brochure Design Project

I need a brochure for my new company "Nine Moons". You can read all about the company at http://www.ninemoons-example.com.sg
On the website you will also get an idea of the concept of the product, as well as design. This design actually comes from a Wordpress theme.
The brochure needs to be like a print version of the website but much more summarised, high-level. I'd like to distribute it to expecting mothers at various locations such as pre-natal yoga classes. The intention is to create enough interest so these moms-to-be will surf to my website and check out what it's all about.
Target Market(s)
Expecting moms and dads (pregnant)
Industry/Entity Type
It Company
Look and feel

```html
<!DOCTYPE html>
<html lang="en">
<head>
<meta charset="utf-8">
<title>Nine Moons Brochure</title>
<link href="https://fonts.googleapis.com/css2?family=Oswald:wght@400;500&family=Arimo:wght@400;700&display=swap" rel="stylesheet">
<style>
:root{
  --blue:#1aa3e4;
  --blue-dark:#1287c4;
  --ink:#2a2a2a;
  --black:#1f1f1f;
  --white:#ffffff;
  --paper:#fafafa;
  --edge:#d8d8d8;
  --photo-light:#dfeef7;
  --photo-mid:#b7d9ee;
}
*{margin:0;padding:0;box-sizing:border-box}
html,body{width:847px;height:1200px;overflow:hidden;background:var(--white)}
body{position:relative;font-family:"Arimo",Arial,sans-serif}
.head{font-family:"Oswald","Arial Narrow",sans-serif;font-weight:500;text-transform:uppercase}

.spread{position:absolute;left:18px;width:811px;background:var(--paper);border:1px solid var(--edge);overflow:hidden}
.spread-outer{top:12px;height:490px}
.spread-inner{top:514px;height:676px;background:var(--white)}

.top-band{position:absolute;left:0;top:6px;width:347px;height:22px;background:var(--blue)}
.portrait{position:absolute;left:147px;top:186px;width:40px;height:40px;background:linear-gradient(135deg,#c9a489,#6b4a3a)}
.about-title{position:absolute;left:0;width:347px;top:230px;text-align:center;color:var(--blue);font-size:12px}
.about-text{position:absolute;left:22px;width:304px;top:252px;color:var(--blue);font-size:6.4px;line-height:7.6px;text-align:center}
.about-text p{margin-bottom:7px}

.cta{position:absolute;left:103px;top:425px;width:136px;height:32px;background:var(--blue);border:2px solid var(--white);border-radius:7px;color:var(--white);font-size:14px;text-align:center;line-height:28px;box-shadow:0 0 0 1px var(--blue)}
.contact-band{position:absolute;left:0;top:456px;width:811px;height:26px;background:var(--blue);color:var(--white);font-size:10.5px;line-height:26px}
.contact-band .phone{position:absolute;left:28px}
.contact-band .site{position:absolute;left:467px}

.tagline{position:absolute;left:360px;width:330px;top:55px;text-align:center;color:var(--blue);font-size:12.5px;line-height:18px}
.hero-photo{position:absolute;left:382px;top:95px;width:292px;height:255px;background:radial-gradient(ellipse at 50% 70%,var(--photo-mid),var(--photo-light) 70%,var(--paper))}
.brand{position:absolute;left:470px;top:358px;color:var(--ink);font-family:"Oswald","Arial Narrow",sans-serif;font-weight:500;font-size:27px}
.brand-sub{position:absolute;left:370px;width:330px;top:420px;text-align:center;color:var(--blue);font-size:11px}

.services{position:absolute;left:0;top:0;width:527px;height:100%;background:var(--blue);color:var(--white)}
.col{position:absolute;top:30px;width:166px;font-size:6.3px;line-height:7.5px}
.col-1{left:18px}.col-2{left:192px}.col-3{left:366px;width:155px}
.col h2{font-family:"Oswald","Arial Narrow",sans-serif;font-weight:500;font-size:11px;line-height:14px;text-transform:uppercase;margin:2px 0 3px}
.col h3{font-family:"Oswald","Arial Narrow",sans-serif;font-weight:500;font-size:6.6px;text-transform:uppercase;margin-top:6px}
.col p{margin-bottom:2px}

.packages{position:absolute;left:527px;top:0;width:284px;height:100%;background:var(--black);color:#bdbdbd;text-align:center;font-size:6.4px;line-height:8px}
.packages-tab{position:absolute;left:33px;top:20px;width:130px;height:30px;background:var(--blue);color:var(--white);font-size:12px;line-height:30px}
.pk-body{position:absolute;left:20px;width:244px;top:60px}
.pk-body p{margin-bottom:6px}
.pk-body h4{font-family:"Oswald","Arial Narrow",sans-serif;font-weight:500;color:var(--white);font-size:10.5px;text-transform:uppercase;margin-top:6px}
.pk-body .dot{color:#777;line-height:6px}
.pk-body .price{color:#e6e6e6;margin-bottom:8px}
</style>
</head>
<body>

<section class="spread spread-outer">
  <div class="top-band"></div>
  <div class="portrait" role="img" aria-label="Small portrait photo of the founder"></div>
  <h2 class="head about-title">About</h2>
  <div class="about-text">
    <p>Nine Moons was founded by Mara Lindqvist who went through her pregnancy realising there was so much out there she wasn't prepared for. Which was normal! But for busy working moms out there, who want this to be a wonderful journey with no stress, some help would have been nice :-)</p>
    <p>Mara got her wedding planned nearly 9 years ago by a wedding planner. There was so much to take care of, they hired the wedding planner months in advance. Having a baby is as huge an event – so why not get someone to help plan that too?</p>
    <p>Being a Project Manager herself in the corporate world, implementing complex IT projects for multi-nationals and managing millions of dollars of budgets, Mara was already equipped with detailed planning skills, ability to juggle multiple ongoing tasks, manage demanding customers and communicate well. That coupled with her passion for the world of babies made this the perfect dream job for her! During her pregnancy (and even after birth) Mara spent countless night reading up and finding out more about pregnancy and the first year. It was baffling how much information there was out there that most moms didn't know, and how much there was to plan and take care of to get ready for the little one!</p>
    <p>That's how Nine Moons was born – to help busy moms and dads with the hard stuff so you can sit back and relax. First time moms get the guidance they need, and experienced parents can spend quality time with their older kids!</p>
  </div>
  <div class="head cta">Ready to start?</div>
  <div class="contact-band">
    <span class="phone">Call 8123-4567 or email me at mara@ninemoons-example.com.sg</span>
    <span class="site">www.ninemoons-example.com.sg</span>
  </div>
  <h1 class="head tagline">Relax.... and let us take care of planning, organising and preparing for the arrival of your little one!</h1>
  <div class="hero-photo" role="img" aria-label="Photo of a baby in a blue bath tub with rubber ducks"></div>
  <div class="brand">Nine Moons</div>
  <div class="head brand-sub">Personalised baby planner &amp; maternity concierge</div>
</section>

<section class="spread spread-inner">
  <div class="services">
    <div class="col col-1">
      <h2>Services</h2>
      <p>The first thing I do is a free telephone or face-to-face consultation at a location of your choice, be that your home, or somewhere we can grab a coffee together. The idea is to get to know you and your pregnancy better, and find out your needs and goals as well as your budget. I'll ask you some questions so that I can get a better idea of your personality as well as your philosophies on health, child-rearing and your environment. A questionnaire will also help me to collect this information. Then I'll explain to you how I can help you. I can be as as active as you wish, or I can be as non-intrusive as you desire – the choice is yours!</p>
      <h2>During your pregnancy...</h2>
      <h3>The Nine Moons Action Plan</h3>
      <p>A personalised binder with a week-by-week action plan created and customised just for you and your pregnancy.</p>
      <h3>Product reviews and suggestions</h3>
      <p>Strollwell or Pramly? Nurturo or Tiny Sips? I'll help you dig for the latest product reviews and guide you in making your selection based on your needs assessment and philosophies.</p>
      <h3>Nursery setup &amp; design</h3>
      <p>Helping you to organise your nursery so you can optimise the space in the best way. Get the layout right so you won't be tripping over things in the middle of the night! Plus creating both a soothing and stimulating environment for your little one.</p>
      <h3>Layette shopping</h3>
      <p>The layette is a newborn's very first wardrobe. I can accompany you and give you tips/advice, or I can do the entire layette shopping for you. All up to you to decide.</p>
      <h3>Blockbaby shower planning</h3>
      <p>From helping you with the design of the invite (online or print) to sending them out, taking care of coordination for food, venue, decorations, rsvps and everything else around planning for the shower.</p>
      <h3>Sourcing for confinement nanny</h3>
      <p>If you have a list you want me to start calling them, I'll start with that. Otherwise I'll check with my own contacts or sources for them for you. Once we have a list, I will give you an overview and we can shortlist together. I'll arrange for interviews so you can have a feel for the nanny. I can also attend the interview together with you if you wish.</p>
    </div>
    <div class="col col-2">
      <h3>Newborn care</h3>
      <p>Hospital checkups don't exactly cover this topic, and our well-meaning elders brought us up well, but some of their methods can be rather outdated. I can walk you through some basic newborn care guidelines. Note that medical issues should always be discussed with your baby's pediatrician.</p>
      <h3>Baby registry setup</h3>
      <p>Although not commonly done in Singapore, more and more parents are interested in a Baby Registry. Friends and family really appreciate the guidance in gift-selection when a Baby Registry is available. Not many baby shops in Singapore provide this service. We can even set one up online for you, so well-meaning gift-givers know exactly what you need.</p>
      <h3>Birth planning</h3>
      <p>How do you want to give birth? Have you decided on pain relief options? Anything you absolutely wish for, or want to avoid? Most mothers forget about this plan and realise it only too late. All these choices should all be mapped out in your birth plan. I can ask you the right questions, and provide you with the right information. I can even draft one for you based on your options.</p>
      <h3>Baby announcement</h3>
      <p>Baby announcements are something else not commonly done by Singaporean parents, but is quickly becoming a trend. I can help you with creative baby announcement ideas, help to select and coordinate not only the design and print of the announcements, but addressing and stamping each envelope and of course sending them out on the big day.</p>
      <h3>Health, happiness &amp; well-being</h3>
      <p>It's important to stay healthy during your pregnancy – and look good while you're at it! I can suggest safety tips for your pregnancy, pre-natal classes, advice on weight gain, sleep difficulties, managing stress and mood swings. For working moms, I can brief you on your rights at work. I'll even help you with maternity shopping – because I know how hard it is to find stylish maternity clothing!</p>
      <h3>Advice &amp; consultation</h3>
      <p>Providing as much information and advice as you need on any topic at all related to preparing for your baby such as pre-natal scans, daddy advice, bonding with your bump, postnatal confinement, etc.</p>
    </div>
    <div class="col col-3">
      <h3>Concierge service</h3>
      <p>All of the above doesn't quite cover it? Maybe you just need an extra helping hand to get things done for you, like getting a petsitter during your hospital stay or getting food delivered in the first weeks you get home with baby.</p>
      <h2>After birth...</h2>
      <h3>Diaper/newborn care (up to 12 mths)</h3>
      <p>Clueless about how to bathe a baby, change a diaper or even to feed? Nervous about handling a newborn for the first time? You'll get some tips at the hospital and some guidance from elders, but it can be handy to get some help. Dads can really benefit from this too. This service is also available before the pregnancy.</p>
      <h3>Postpartum support</h3>
      <p>Everyone talks about and focuses on the great stuff, the glow of a new mom, the wonder of a newborn. And who would blame them, I'd do it all over again. But being a new parent can have a darker side no one seems to talk about in the open. It can help to know you are not the only one questioning why you sometimes feel so down, and why breastfeeding isn't as serene and calm an experience as the "breast is best" posters seem to depict.</p>
      <h3>Asian confinement traditions</h3>
      <p>Confinement nanny for the Chinese? Massage (urut) for the Malays? Special confinement diet for the Indians? If you need help with contacts or just information, I can help out.</p>
      <h3>Nanny / childcare sourcing</h3>
      <p>Once you have to go back to work, some will have grandma &amp; grandpa watch the baby, or the maid. But not all are lucky enough to have this, or may have a maid who is a brilliant help at home but clueless with babies. Sourcing for a nanny of childcare can be challenging and I can help you from sourcing all the way to shortlisting and interviewing.</p>
      <h3>Baby food making</h3>
      <p>It's so easy to make your own baby food. I can show you how to introduce your baby to exciting flavours, share recipes and create a meal plan for baby (4 months old onwards). I can even go as far as making and freezing one week's worth of baby food at a time, using your own kitchen.</p>
    </div>
  </div>
  <div class="packages">
    <div class="head packages-tab">Packages</div>
    <div class="pk-body">
      <p>You can choose to pick a service à-la-carte at an hourly rate of $75/hour, or you can get one of the packages below.</p>
      <p>All of our packages include:<br>A 1-hour telephone or face-to-face session to get to know you and your needs</p>
      <p>Free unlimited email and phone (10 mins or less) consultations for 1 month from the date of the original consult</p>
      <h4>Baby Step</h4>
      <p>A customised "Nine Moons Action Plan"</p>
      <p class="dot">•</p>
      <p>A face-to-face presentation and explanation of the "Nine Moons Action Plan"</p>
      <p class="price">Price: $180</p>
      <h4>5-Star Nest</h4>
      <p>Nursery setup and design</p>
      <p class="dot">•</p>
      <p>Layette shopping</p>
      <p class="price">Price: $280</p>
      <h4>Bundle of Joy</h4>
      <p>1-hour Newborn Care workshop</p>
      <p class="dot">•</p>
      <p>Product reviews/suggestions for 5 chosen newborn products</p>
      <p class="dot">•</p>
      <p>Birth planning</p>
      <p class="price">Price: $350</p>
      <h4>Pamper Hamper</h4>
      <p>Baby shower planning (invites, menu planning, shopping, thank-you notes, games, actual day coordination)</p>
      <p class="dot">•</p>
      <p>Baby registry setup (including online tool)</p>
      <p class="dot">•</p>
      <p>Baby announcement (collecting addresses, design, mailing)</p>
      <p class="dot">•</p>
      <p>1-hour Health, Happiness &amp; Well-Being workshop</p>
      <p class="price">Price: $500</p>
    </div>
  </div>
</section>

</body>
</html>
```